Beauty Salon Design

The business card design will be for a new beauty salon opening up.

The therapist has over 11 years at a leading beauty Salon in perth.

The two colours that the salon will use is black and gold.

Industry/Entity Type

Beauty Salon

Contact Information for Business Card

Velmora Beauty

Corinne Ashdale
Advanced beauty therapist
0457 318 042

Monday - Friday 9am - 2.30pm
Weekends and nights by appointment only

Waxing, Tinting, Swedish massage, hot stone massage, facials, peels, micro, LED light treatment, skin needling and retail products.

```html
<!DOCTYPE html>
<html lang="en">
<head>
<meta charset="utf-8">
<title>Velmora Beauty – Business Card</title>
<link rel="stylesheet" href="https://fonts.googleapis.com/css2?family=Josefin+Sans:wght@300;400&display=swap">
<style>
  :root {
    --stage: #4b5356;
    --card-black: #0b0b0b;
    --card-charcoal: #1a1c1d;
    --gold: #b7b000;
    --gold-bright: #e6e600;
    --gold-deep: #8c8300;
    --gold-text: #d8cf1a;
    --muted-olive: #5f5a10;
    --ink: #1a1a1a;
    --name-light: #f1ea9c;
  }
  * { margin: 0; padding: 0; box-sizing: border-box; }
  html, body {
    width: 1200px; height: 741px; overflow: hidden;
    background: var(--stage);
    font-family: "Josefin Sans", "Helvetica Neue", Arial, sans-serif;
  }
  .stage { position: relative; width: 1200px; height: 741px; }

  .card {
    position: absolute;
    left: 395px;
    width: 410px; height: 236px;
    overflow: hidden;
    background: var(--card-black);
    box-shadow: 0 10px 24px rgba(0,0,0,.45);
  }
  .card--front { top: 88px; }
  .card--back  { top: 412px; background: linear-gradient(180deg, var(--card-charcoal), var(--card-black)); }

  .card__wave { position: absolute; inset: 0; width: 100%; height: 100%; }

  /* front */
  .card__artwork {
    position: absolute; left: 30px; top: 0;
    width: 300px; height: 212px;
    border-radius: 0 0 60px 140px;
    background: radial-gradient(ellipse at 35% 40%, #2a2608 0%, #0b0b0b 65%);
  }
  .card__phone {
    position: absolute; top: 9px; right: 12px;
    display: flex; align-items: center; gap: 6px;
    font-size: 13px; letter-spacing: 1.5px;
    color: var(--gold-bright);
  }
  .card__phone svg { width: 9px; height: 14px; }
  .card__brand {
    position: absolute; right: 16px; bottom: 18px;
    font-size: 27px; font-weight: 400;
    color: var(--gold);
    letter-spacing: 1px;
  }

  /* back */
  .card__hours {
    position: absolute; top: 8px; right: 12px;
    font-size: 11px; color: var(--ink);
  }
  .card__person { position: absolute; right: 14px; top: 62px; text-align: right; }
  .card__name { font-size: 17px; font-weight: 400; color: var(--name-light); }
  .card__role { font-size: 14px; font-weight: 300; color: var(--gold); margin-top: 3px; }
  .card__services {
    position: absolute; left: 20px; top: 124px;
    list-style: none;
    font-size: 11px; font-weight: 300; line-height: 18px;
    color: var(--muted-olive);
  }
  .card__services span { margin-right: 8px; }
  .card__footer {
    position: absolute; left: 0; bottom: 0;
    width: 100%; height: 17px;
    padding: 3px 4px 0;
    font-size: 10px; color: var(--ink);
    background: linear-gradient(90deg, var(--gold-bright) 0%, var(--gold) 45%, var(--gold-deep) 100%);
  }
</style>
</head>
<body>
<main class="stage">

  <section class="card card--front">
    <svg class="card__wave" viewBox="0 0 410 236" preserveAspectRatio="none" aria-hidden="true">
      <defs>
        <linearGradient id="frontGold" x1="0" y1="0" x2="0" y2="1">
          <stop offset="0" stop-color="#a29a00"/>
          <stop offset="1" stop-color="#d6d200"/>
        </linearGradient>
      </defs>
      <path d="M0 0 H410 V40 C330 62 250 60 180 58 C110 56 40 120 0 180 Z" fill="url(#frontGold)"/>
    </svg>
    <div class="card__artwork" role="img" aria-label="Illustration of a woman with long flowing black hair and a red highlight"></div>
    <p class="card__phone">
      <svg viewBox="0 0 9 14" aria-hidden="true"><rect x="0.5" y="0.5" width="8" height="13" rx="1.5" fill="#111" stroke="#e6e600"/><rect x="2" y="2.5" width="5" height="5" fill="#e6e600"/></svg>
      0457 318 042
    </p>
    <h1 class="card__brand">Velmora Beauty</h1>
  </section>

  <section class="card card--back">
    <svg class="card__wave" viewBox="0 0 410 236" preserveAspectRatio="none" aria-hidden="true">
      <defs>
        <linearGradient id="backGold" x1="0" y1="0" x2="0" y2="1">
          <stop offset="0" stop-color="#b3ad00"/>
          <stop offset="1" stop-color="#f0f000"/>
        </linearGradient>
      </defs>
      <path d="M0 0 H410 V42 C340 44 280 50 220 64 C150 80 80 78 0 58 Z" fill="url(#backGold)"/>
    </svg>
    <p class="card__hours">Monday - Friday 9am - 2.30pm</p>
    <div class="card__person">
      <h2 class="card__name">Corinne Ashdale</h2>
      <p class="card__role">Advanced beauty therapist</p>
    </div>
    <ul class="card__services">
      <li>hot stone massage</li>
      <li><span>skin needling</span>swedish massage</li>
      <li><span>retail products</span><span>waxing</span>tinting</li>
      <li>facials, peels, micro LED light treatment</li>
    </ul>
    <p class="card__footer">Weekends and nights by appointment only</p>
  </section>

</main>
</body>
</html>
```